Visitenkarten für Psychotherapeutin
Zielgruppe
Ich war Psychologin und Coachin und bin jetzt eine approbierte Psychotherapeutin.
Aufgabenstellung
Es gibt ein Layout, an das sich angelehnt werden soll.
Die Farb- und Schriftwelt liegt vor, jedoch soll aus dem türkies ein warmer Pink-Rot-Ton werden.
Die Visitenkarte soll für die neu eröffnete Privatpraxis verwendet werden. Im Logo soll die Berufsbezeichnung Psychologische Psychotherapeutin (mit) Schwerpunkt Systemische Therapie stehen.
Neben den Kontaktdaten folgender Text:
Privatpraxis für Psychologische Psychotherapie, Schwerpunkt Systemische Therapie
Für Privatversicherte und Selbstzahlende
Termin nach Vereinbarung
Die Zeile mit der Sprechstunde soll weg.

```html
<!DOCTYPE html>
<html lang="de">
<head>
<meta charset="utf-8">
<title>Visitenkarte Hanna Morbach</title>
<link href="https://fonts.googleapis.com/css2?family=Montserrat:wght@400;500;600;700&display=swap" rel="stylesheet">
<style>
  :root {
    --backdrop: #b1a896;
    --paper: #fbfbfa;
    --brand-pink: #cd1150;
    --ink: #1b1b1b;
    --white: #ffffff;
  }
  * { margin: 0; padding: 0; box-sizing: border-box; }
  html, body {
    width: 1200px; height: 800px; overflow: hidden;
    background: var(--backdrop);
    font-family: "Montserrat", Arial, sans-serif;
  }
  .canvas { position: relative; width: 1200px; height: 800px; }
  .card {
    position: absolute; top: 232px;
    width: 520px; height: 336px; overflow: hidden;
  }
  .card--contact { left: 50px; background: var(--paper); color: var(--ink); }
  .card--front { left: 630px; background: var(--brand-pink); color: var(--white); }

  .contact-name {
    position: absolute; left: 56px; top: 88px;
    font-size: 36px; font-weight: 500; color: var(--brand-pink);
    letter-spacing: 0.5px;
  }
  .contact-lines {
    position: absolute; left: 56px; top: 154px;
    font-size: 16.5px; font-weight: 500; line-height: 1.4;
    font-style: normal;
  }
  .contact-note {
    position: absolute; left: 56px; top: 260px;
    font-size: 13px; font-weight: 700; letter-spacing: 1.2px;
    color: var(--brand-pink); text-transform: uppercase;
  }

  .front-mark {
    position: absolute; left: 0; right: 0; top: 100px; text-align: center;
  }
  .front-name {
    font-size: 36px; font-weight: 500; letter-spacing: 0.5px;
  }
  .front-tagline {
    margin-top: 8px;
    font-size: 8.5px; font-weight: 600; letter-spacing: 2.4px; line-height: 1.6;
    text-transform: uppercase;
  }
  .front-services {
    position: absolute; left: 28px; right: 20px; top: 242px;
    text-transform: uppercase;
  }
  .front-services .practice {
    font-size: 13.5px; font-weight: 700; letter-spacing: 0.4px; line-height: 1.25;
  }
  .front-services .audience {
    margin-top: 8px;
    font-size: 12px; font-weight: 500; letter-spacing: 0.4px;
  }
</style>
</head>
<body>
  <main class="canvas">
    <section class="card card--contact" aria-label="Rückseite mit Kontaktdaten">
      <p class="contact-name">Hanna Morbach</p>
      <address class="contact-lines">
        Lindenweg 12 . 82040 Tannried<br>
        T. +49 170 5550142 | kontakt@hmorbachtu.de<br>
        www.hmorbachtu.de
      </address>
      <p class="contact-note">Termin nach Vereinbarung</p>
    </section>

    <section class="card card--front" aria-label="Vorderseite">
      <div class="front-mark">
        <p class="front-name">Hanna Morbach</p>
        <p class="front-tagline">Psychologische Psychotherapeutin<br>Schwerpunkt Systemische Therapie</p>
      </div>
      <div class="front-services">
        <p class="practice">Privatpraxis für Psychologische Psychotherapie<br>Schwerpunkt: Systemische Therapie</p>
        <p class="audience">Privatversicherte | Beihilfeberechtigte | Selbstzahlende</p>
      </div>
    </section>
  </main>
</body>
</html>
```